Require stationery design which includes the following items as a minimum.

- Business card design
- Letterhead
- Envelopes

Details for business card:
Logo: Main logo is called "dove interiors square gold" but you may make use of whichever logo works best.
Tagline: Exquisite Furniture & Furnishings
Name: Helen Marchetti
Title: Interior Stylist
Mobile: 0432 871 264
PH: 03 9572 3140
Email: helen@dove-interiors.com.au

```html
<!DOCTYPE html>
<html lang="en">
<head>
<meta charset="utf-8">
<title>Dove Interiors — Business Cards</title>
<link href="https://fonts.googleapis.com/css2?family=Tinos:wght@400&display=swap" rel="stylesheet">
<style>
  :root {
    --backdrop: #2f2725;
    --card: #141312;
    --card-edge: #0b0a0a;
    --gold: #d8bc6a;
    --gold-soft: #b99a4e;
  }
  * { margin: 0; padding: 0; box-sizing: border-box; }
  html, body { width: 1200px; height: 716px; overflow: hidden; }
  body {
    background: var(--backdrop);
    font-family: "Tinos", "Times New Roman", serif;
    color: var(--gold);
  }
  .canvas {
    width: 1200px;
    height: 716px;
    display: flex;
    align-items: center;
    justify-content: center;
    gap: 60px;
  }
  .card {
    width: 510px;
    height: 292px;
    background: var(--card);
    border: 1px solid var(--card-edge);
    box-shadow: 0 18px 40px rgba(0,0,0,0.45);
    display: flex;
    flex-direction: column;
    align-items: center;
    justify-content: center;
    text-align: center;
  }
  .brand-mark {
    width: 36px;
    height: 36px;
    border: 2px solid var(--gold);
    margin-bottom: 16px;
  }
  .brand-name {
    font-size: 36px;
    font-weight: 400;
    letter-spacing: 0.1em;
    text-transform: uppercase;
    line-height: 1;
  }
  .divider-ornament {
    display: block;
    width: 54px;
    height: 12px;
    background: var(--gold-soft);
    border-radius: 6px;
    opacity: 0.8;
    margin: 16px auto;
  }
  .tagline {
    font-size: 17px;
    font-weight: 400;
  }
  .person-name {
    font-size: 24px;
    font-weight: 400;
    text-transform: uppercase;
    letter-spacing: 0.02em;
    line-height: 1.1;
  }
  .person-title {
    font-size: 17px;
    margin-top: 2px;
  }
  .contact-list {
    list-style: none;
    font-size: 17px;
    line-height: 1.3;
  }
  .contact-list .label {
    text-transform: uppercase;
    margin-right: 8px;
  }
</style>
</head>
<body>
  <main class="canvas">
    <section class="card card--brand" aria-label="Business card front">
      <div class="brand-mark" aria-hidden="true"></div>
      <h1 class="brand-name">Dove Interiors</h1>
      <span class="divider-ornament" role="img" aria-label="Gold flourish ornament"></span>
      <p class="tagline">Exquisite Furniture &amp; Furnishings</p>
    </section>

    <section class="card card--contact" aria-label="Business card back">
      <div class="brand-mark" aria-hidden="true"></div>
      <h2 class="person-name">Helen Marchetti</h2>
      <p class="person-title">Interior Stylist</p>
      <span class="divider-ornament" role="img" aria-label="Gold flourish ornament"></span>
      <ul class="contact-list">
        <li><span class="label">Mobile</span>0432 871 264</li>
        <li><span class="label">Phone</span>03 9572 3140</li>
        <li>helen@dove-interiors.com.au</li>
      </ul>
    </section>
  </main>
</body>
</html>
```